Executive Business Card for Healthcare Company [Need Today]

I need a business card design for a healthcare company. The only branding the company has thus far is a logo. The cards will be utilized by company executives. The design I envision will be vibrant and appealing but with a corporate feel. They shouldn't be too casual or playful. I would like to complete this project TODAY if possible.

Target Market(s)

Healthcare vendors, other executives in healthcare and pharmaceuticals

Industry/Entity Type

Pharmaceutical

Contact Information for Business Card

See attachment

Font styles to use
Serif
Sans Serif

Colors

Designer to choose colors to be used in the design.

```html
<!DOCTYPE html>
<html lang="en">
<head>
<meta charset="utf-8">
<title>Verana Therapeutics – Executive Business Card</title>
<link rel="stylesheet" href="https://fonts.googleapis.com/css2?family=Open+Sans:wght@300;400;600;700&display=swap">
<style>
  :root {
    --teal: #3bbfc4;
    --teal-dark: #2aa8b0;
    --mint: #6cc89a;
    --aqua: #47bcc6;
    --ink: #5c5c5c;
    --paper: #ffffff;
    --backdrop: #ecebe7;
  }
  * { box-sizing: border-box; margin: 0; padding: 0; }
  html, body {
    width: 1200px; height: 1000px; overflow: hidden;
    background: var(--backdrop);
    font-family: "Open Sans", Arial, sans-serif;
  }
  .sheet {
    width: 1200px; height: 1000px;
    display: flex; flex-direction: column; align-items: center; justify-content: center;
    gap: 60px;
  }
  .card {
    width: 630px; height: 360px;
    position: relative; overflow: hidden;
    box-shadow: 0 6px 18px rgba(0,0,0,.18);
  }

  /* Back of card */
  .card-back {
    background: linear-gradient(150deg, var(--mint) 0%, var(--aqua) 100%);
  }
  .card-back .pattern {
    position: absolute; inset: 0;
    background:
      radial-gradient(circle at 25% 30%, rgba(255,255,255,.16), transparent 45%),
      radial-gradient(circle at 80% 75%, rgba(150,210,255,.22), transparent 50%);
  }
  .card-back .brand {
    position: absolute; left: 50%; top: 50%;
    transform: translate(-50%, -50%);
    display: flex; align-items: center; gap: 18px;
    color: var(--paper);
  }
  .brand .dot {
    width: 78px; height: 78px; border-radius: 50%;
    border: 3px solid currentColor; flex: none;
  }
  .brand .rule { width: 2px; height: 70px; background: currentColor; }
  .brand .name {
    font-size: 34px; font-weight: 300; line-height: 1.05; letter-spacing: .5px;
  }

  /* Front of card */
  .card-front { background: var(--paper); }
  .card-front .edge {
    position: absolute; left: 0; right: 0; bottom: 0; height: 14px;
    background: var(--teal);
  }
  .card-front .brand {
    position: absolute; left: 40px; top: 34px;
    display: flex; align-items: center; gap: 14px;
    color: var(--teal);
  }
  .card-front .brand .dot { width: 60px; height: 60px; border-color: var(--mint); }
  .card-front .brand .rule { height: 52px; background: var(--teal); }
  .card-front .brand .name { font-size: 28px; }
  .card-front .divider {
    position: absolute; left: 40px; top: 118px; width: 330px; height: 2px;
    background: var(--teal);
  }
  .person {
    position: absolute; right: 40px; top: 130px; text-align: right;
  }
  .person .full-name {
    font-size: 24px; font-weight: 600; letter-spacing: 1.5px;
    color: var(--teal); text-transform: uppercase;
  }
  .person .role {
    font-size: 15px; color: var(--ink); margin-top: 2px;
  }
  .contacts {
    position: absolute; left: 40px; bottom: 40px;
    list-style: none; font-size: 14px; color: var(--ink); line-height: 1.45;
  }
  .contacts li { display: flex; align-items: center; gap: 8px; }
  .contacts svg { width: 12px; height: 12px; flex: none; }
  .contacts .company { font-weight: 700; margin-top: 4px; }
  .contacts .plain { padding-left: 0; }
</style>
</head>
<body>
<main class="sheet">

  <section class="card card-back" aria-label="Card back">
    <div class="pattern" role="img" aria-label="Soft pattern of large looping brand flourishes in pale blue and white"></div>
    <div class="brand">
      <span class="dot"></span>
      <span class="rule"></span>
      <span class="name">Verana<br>therapeutics</span>
    </div>
  </section>

  <section class="card card-front" aria-label="Card front">
    <div class="brand">
      <span class="dot"></span>
      <span class="rule"></span>
      <span class="name">Verana<br>therapeutics</span>
    </div>
    <div class="divider"></div>

    <div class="person">
      <p class="full-name">Daniel Moreau</p>
      <p class="role">Senior Director of Marketing</p>
    </div>

    <ul class="contacts">
      <li>
        <svg viewBox="0 0 12 12"><rect x="3" y="1" width="6" height="10" rx="1" fill="none" stroke="var(--teal)" stroke-width="1.4"/></svg>
        555-201-4477
      </li>
      <li>
        <svg viewBox="0 0 12 12"><path d="M2 1.5h2.5l1 2.5-1.3 1a6 6 0 0 0 2.8 2.8l1-1.3 2.5 1V10a1 1 0 0 1-1 1A8.5 8.5 0 0 1 1 2.5a1 1 0 0 1 1-1z" fill="var(--teal)"/></svg>
        555-318-6620
      </li>
      <li>
        <svg viewBox="0 0 12 12"><rect x="0.5" y="2" width="11" height="8" fill="var(--teal)"/><path d="M1 2.5l5 4 5-4" fill="none" stroke="#fff" stroke-width="1.2"/></svg>
        dmoreau@veranarx.com
      </li>
      <li class="company">Verana Therapeutics, LLC</li>
      <li>118 Linden Avenue</li>
      <li>Riverton, GA 30012</li>
    </ul>

    <div class="edge"></div>
  </section>

</main>
</body>
</html>
```